Website Design for a Graphic Design Studio in California

We are working with a graphic design company in California.
PLEASE NOTE: We report and ban any designer that reaches out directly to our customers.

Some sites to use for content/competitors and inspiration:

http://quelvint.co.uk
https://www.fendro.studio
https://www.zuplo.io (Client's Favorite)
https://www.merigoldcrafts.com
https://craftwimble.com
https://www.dravinsultonmask.com/us/home/

Thank you for taking the time to consider designing a website for us. We are web developers based in Stockton, CA, USA. Most of our projects go through the same process. Understanding this process may help you win a project with us. We custom-code all of our websites in-house. We don’t have any requirements as to what tools you use for your design, but we prefer Figma files. For any design that we label as four-stars, we send it to the client for review. The client picks the final design they want us to use. Once we complete this process, we will continue to show additional clients all the four-star sites and purchase them later. Your designs will have multiple chances to sell. For better chances of success, we ask that you follow these guidelines.

IMAGES:
If you use any images or icons in the design, we ask that you have a link to the asset so we can purchase the image/icon. Most of the designs we submit do not have the customer’s images on them unless they have some great images. Be creative; show us the feeling you are trying to portray with your image choices. Use any royalty-free site you choose. We subscribe to Tessaly and mainly use their images, but we can purchase images outside of Tessaly. PLEASE NOTE: we will not submit designs to clients with watermarks on the images.

FONTS:
We ask that you identify the fonts used in the design. This can be done in a message if you want. We typically use Brindle Fonts and Tessaly Fonts.

CONTENT:
We're always open to different content and ideas. We often submit designs with stock images so the client can see our vision. We typically take pictures after the website launch to use their images with our vision. Lorem Ipsum is fine for paragraphs, but we ask that you write the headers in correct English. We want to be able to show the vision and identify the sections of the website.

INSPIRATION:
We typically add a couple of links in the brief of websites we like to help you get started in your design.

REVISIONS:
We do not often ask for revisions of the designs unless we see something in the design that may not appeal to the client. If there are slight changes that we want to make, we do that in the development process.

FEEDBACK:
We rarely give feedback on designs during the design process. We are working on many website projects and do not have the time to provide feedback. We usually respond if your request is well thought out and asks specific questions, but a note asking “feedback, please” usually goes unanswered.

```html
<!DOCTYPE html>
<html lang="en">
<head>
<meta charset="utf-8">
<title>Morrowline Creative — Building Your Brand</title>
<link href="https://fonts.googleapis.com/css2?family=Cinzel:wght@400;500;600&family=Montserrat:wght@400;500;600;700&display=swap" rel="stylesheet">
<style>
:root{
  --gold:#d9a536;
  --gold-soft:#f3e3bd;
  --ink:#1f1f1f;
  --muted:#555;
  --mist:#f1f5f5;
  --night:#1b1b1b;
  --white:#fff;
  --slate:#5b6670;
}
*{box-sizing:border-box;margin:0;padding:0}
html,body{width:1200px;height:5177px;overflow:hidden}
body{font-family:"Montserrat",Arial,sans-serif;color:var(--ink);background:var(--white);position:relative}
.abs{position:absolute}
section,header,footer{position:absolute;left:0;width:1200px}
.mark-dot{display:inline-block;border-radius:50%;border:5px solid var(--slate)}
.section-title{display:flex;align-items:center;gap:18px;font-family:"Cinzel",Georgia,serif;color:var(--gold);font-weight:500;white-space:nowrap}

/* header */
.site-header{top:0;height:145px;background:var(--white)}
.brand{left:80px;top:56px;display:flex;align-items:center;gap:10px;font-family:"Cinzel",serif;color:var(--gold);font-size:21px;letter-spacing:1px}
.brand .mark-dot{width:34px;height:34px;border-width:4px}
.nav{right:86px;top:66px;display:flex;gap:29px;font-size:13px;color:#333}
.nav .active{color:var(--gold)}

/* hero */
.hero{top:145px;height:748px}
.hero-photo{position:absolute;inset:0;background:linear-gradient(160deg,#5a4a3a 0%,#3b3026 40%,#6e5c4b 70%,#2e2620 100%)}
.hero-shade{position:absolute;inset:0;background:rgba(20,14,8,.35)}
.hero-title{top:308px;width:100%;text-align:center;color:var(--white);font-family:"Cinzel",serif;font-size:74px;font-weight:500;letter-spacing:1px}
.hero-sub{top:380px;width:100%;text-align:center;color:var(--gold);font-size:50px;font-weight:500}

/* about */
.about{top:893px;height:730px}
.about .section-title{left:78px;top:122px;font-size:58px}
.about .mark-dot{width:62px;height:62px;border-width:6px}
.about-lead{left:78px;top:253px;width:500px;font-size:21.5px;line-height:38px;font-weight:500}
.about-body{left:78px;top:434px;width:490px;font-size:12.8px;line-height:22.5px}
.about-photo-back{left:698px;top:129px;width:410px;height:446px;border-radius:14px;background:linear-gradient(150deg,#7a5a36,#c49766 50%,#d8d2c8)}
.about-photo-front{left:664px;top:353px;width:332px;height:270px;border-radius:14px;border:4px solid var(--white);background:linear-gradient(160deg,#bcb7a8,#8c8476 55%,#514a40)}

/* capabilities */
.capabilities{top:1623px;height:730px;background:var(--mist)}
.capabilities .section-title{left:345px;top:137px;font-size:40px;letter-spacing:1px}
.capabilities .mark-dot{width:50px;height:50px;border-width:5px}
.cap-label{font-size:27px;color:#333;font-weight:500;line-height:32px}
.cap-disc-name{width:440px;left:397px;top:450px;text-align:center;font-family:"Cinzel",serif;font-weight:500;color:var(--gold);font-size:42px;line-height:54px;letter-spacing:3px}

/* process */
.process{top:2353px;height:940px}
.process .section-title{left:364px;top:80px;font-size:60px}
.process .mark-dot{width:62px;height:62px;border-width:6px}
.process-sub{top:168px;width:100%;text-align:center;font-size:32px;font-weight:500}
.stage{width:322px;height:445px;border:1.5px dashed var(--gold);top:302px}
.stage-head{position:absolute;left:0;top:0;width:100%;height:87px;background:var(--gold);padding:7px}
.stage-head span{display:block;height:100%;border:2px solid var(--white);color:var(--white);font-family:"Cinzel",serif;font-size:37px;text-align:center;line-height:68px}
.step{position:absolute;left:20px;display:flex;align-items:center;gap:10px;font-size:15.5px;font-weight:600;white-space:nowrap}
.step b{color:var(--gold);font-weight:600}
.step-icon{width:82px;height:82px;border-radius:50%;border:2px solid var(--gold);display:flex;align-items:center;justify-content:center}
.step-icon i{width:60px;height:60px;border-radius:50%;background:var(--gold);display:block}

/* client project */
.projects{top:3293px;height:880px}
.projects .section-title{left:326px;top:94px;font-size:58px}
.projects .mark-dot{width:62px;height:62px;border-width:6px}
.projects-sub{top:176px;width:100%;text-align:center;font-size:33px;font-weight:500;padding-left:14px}
.card{top:270px;width:300px;height:362px;background:var(--white);border-radius:14px;box-shadow:0 2px 12px rgba(0,0,0,.16);padding:8px;text-align:center}
.card-photo{height:222px;border-radius:6px}
.card h3{color:var(--gold);font-weight:500;font-size:19px;margin-top:32px}
.card p{font-size:13.5px;line-height:23px;margin-top:4px}
.btn{left:481px;top:3955px;width:239px;height:80px;background:var(--gold);color:var(--white);font-size:21px;font-weight:600;display:flex;align-items:center;justify-content:center;gap:12px}

/* testimonial */
.testimonial{top:4173px;height:580px}
.testimonial .section-title{left:360px;top:121px;font-size:54px}
.testimonial .mark-dot{width:62px;height:62px;border-width:6px}
.quote-mark{left:888px;top:64px;font-family:Georgia,serif;font-size:200px;color:#c9c9c9;line-height:1}
.testimonial-sub{top:202px;width:100%;text-align:center;font-size:33px;font-weight:500}
.testimonial-text{left:265px;top:297px;width:670px;text-align:center;font-size:13.4px;line-height:23px}
.avatar{left:494px;top:370px;width:64px;height:64px;border-radius:50%;background:linear-gradient(#d9d9d9,#7d7d7d)}
.person{left:574px;top:388px;font-size:12px}
.person b{color:var(--gold);font-weight:600;display:block}
.person span{font-size:10px;font-weight:600}
.dots{left:537px;top:4653px;display:flex;gap:7px}
.dots i{width:11px;height:11px;border-radius:50%;border:1.5px solid var(--gold);display:block}
.dots i.on{background:var(--gold)}

/* footer */
.site-footer{top:4753px;height:367px;background:var(--night);color:var(--white)}
.foot-brand{left:90px;top:150px;width:215px;text-align:center;font-family:"Cinzel",serif;font-weight:500;color:var(--gold);font-size:24px;line-height:32px;letter-spacing:2px}
.social{left:132px;top:268px;display:flex;gap:7px}
.social i{width:31px;height:31px;border:1.5px solid var(--gold);border-radius:3px;display:block}
.foot-col h4{font-size:12.5px;font-weight:600;letter-spacing:.3px}
.foot-col h4::after{content:"";display:block;width:34px;height:2px;background:var(--gold);margin-top:13px}
.foot-col ul{list-style:none;margin-top:27px}
.foot-col li{font-size:12.5px;display:flex;align-items:center;gap:10px;margin-bottom:11px}
.foot-col li .dot{width:15px;height:15px;border-radius:50%;border:1.5px solid #bbb}
.contact-row{display:flex;gap:14px;font-size:12px;line-height:15px;margin-bottom:18px}
.contact-row .ic{width:26px;height:26px;border:1.5px solid #aaa;border-radius:4px;display:flex;align-items:center;justify-content:center;flex:none}
.news-input{width:186px;height:33px;background:var(--white);margin-top:16px}
.news-btn{width:110px;height:32px;background:var(--gold);font-size:11px;font-weight:600;display:flex;align-items:center;justify-content:center;margin-top:10px}
.copyright{top:5120px;left:0;width:1200px;height:57px;background:var(--gold);color:var(--white);font-size:11.5px;text-align:center;line-height:57px}
</style>
</head>
<body>

<header class="site-header">
  <div class="brand abs"><span class="mark-dot"></span>Morrowline Creative</div>
  <nav class="nav abs"><span class="active">Home</span><span>About Us</span><span>Services</span><span>Process</span><span>Pricing Plans</span><span>Client Projects</span><span>Contact Us</span></nav>
</header>

<section class="hero">
  <div class="hero-photo" role="img" aria-label="Overhead photo of a designer's desk with monitor, sketchbook, pens and sticky notes"></div>
  <div class="hero-shade"></div>
  <h1 class="hero-title abs">Building YOUR Brand</h1>
  <p class="hero-sub abs">One Step at a Time</p>
</section>

<section class="about">
  <h2 class="section-title abs"><span class="mark-dot"></span>About Us</h2>
  <p class="about-lead abs">As a full-service branding and package design agency. We are experts at increasing the value of your brand with imagination, ingenuity and passion.</p>
  <p class="about-body abs">We know that for your business to thrive, all aspects of your branding &amp; marketing need to work together. That's why our proven process builds from the research phase to final asset delivery. Our team makes sure that everything we create for you speaks directly to your ideal customer &amp; helps support your business goals.</p>
  <div class="about-photo-back abs" role="img" aria-label="Photo of hands sketching beside a laptop"></div>
  <div class="about-photo-front abs" role="img" aria-label="Photo of a desk with keyboard, sticky notes and sketches"></div>
</section>

<section class="capabilities">
  <h2 class="section-title abs"><span class="mark-dot"></span>Our Capabilities</h2>
  <svg class="abs" style="left:0;top:0" width="1200" height="730" viewBox="0 0 1200 730">
    <path d="M337 589 A280 280 0 0 1 897 589 Z" fill="#fff" stroke="#f3e3bd" stroke-width="1.5"/>
    <path d="M392 589 A225 225 0 0 1 842 589 Z" fill="#262824"/>
    <g fill="#fff" stroke="#d9a536" stroke-width="2">
      <circle cx="518" cy="317" r="34"/><circle cx="718" cy="313" r="34"/>
      <circle cx="382" cy="409" r="34"/><circle cx="828" cy="413" r="34"/>
      <circle cx="334" cy="529" r="34"/><circle cx="876" cy="537" r="34"/>
    </g>
    <g fill="#d9a536">
      <circle cx="518" cy="317" r="26"/><circle cx="718" cy="313" r="26"/>
      <circle cx="382" cy="409" r="26"/><circle cx="828" cy="413" r="26"/>
      <circle cx="334" cy="529" r="26"/><circle cx="876" cy="537" r="26"/>
    </g>
    <g fill="none" stroke="#fff" stroke-width="2">
      <rect x="506" y="305" width="24" height="24" rx="2"/>
      <rect x="709" y="301" width="18" height="24" rx="2"/><path d="M713 309h10M713 315h10M713 320h6"/>
      <rect x="371" y="398" width="22" height="22" rx="3"/>
      <rect x="816" y="402" width="24" height="18" rx="2"/><path d="M822 425h12"/>
      <circle cx="334" cy="529" r="11"/><path d="M334 518v22M323 529h22"/>
      <rect x="866" y="526" width="20" height="22" rx="2"/><path d="M870 534h12M870 540h12"/>
    </g>
  </svg>
  <div class="cap-disc-name abs">Morrowline<br>Creative</div>
  <div class="cap-label abs" style="left:321px;top:299px">Packaging</div>
  <div class="cap-label abs" style="left:772px;top:297px">Style Guides</div>
  <div class="cap-label abs" style="left:173px;top:393px">Logo Design</div>
  <div class="cap-label abs" style="left:880px;top:393px">Illustration</div>
  <div class="cap-label abs" style="left:134px;top:498px;text-align:right">Branding &amp;<br>Strategy</div>
  <div class="cap-label abs" style="left:925px;top:500px">Marketing<br>Collateral</div>
</section>

<section class="process">
  <h2 class="section-title abs"><span class="mark-dot"></span>Our Process</h2>
  <p class="process-sub abs">9 steps to YOUR rebrand.</p>

  <div class="stage abs" style="left:72px">
    <div class="stage-head"><span>Discover</span></div>
    <div class="step" style="top:135px"><span class="step-icon"><i></i></span><span><b>01</b> Launch Project</span></div>
    <div class="step" style="top:243px"><span class="step-icon"><i></i></span><span><b>02</b> Determine Goal</span></div>
    <div class="step" style="top:347px"><span class="step-icon"><i></i></span><span><b>03</b> Formulate Plan</span></div>
  </div>
  <div class="stage abs" style="left:433px">
    <div class="stage-head"><span>Develop</span></div>
    <div class="step" style="top:140px"><span class="step-icon"><i></i></span><span><b>04</b> Analyse Brand</span></div>
    <div class="step" style="top:238px"><span class="step-icon"><i></i></span><span><b>05</b> Define Identity</span></div>
    <div class="step" style="top:342px"><span class="step-icon"><i></i></span><span><b>06</b> Present Creative</span></div>
  </div>
  <div class="stage abs" style="left:790px">
    <div class="stage-head"><span>Deliver</span></div>
    <div class="step" style="top:143px"><span class="step-icon"><i></i></span><span><b>07</b> Finalize Creative</span></div>
    <div class="step" style="top:243px"><span class="step-icon"><i></i></span><span><b>08</b> Deliver Toolkit</span></div>
    <div class="step" style="top:342px"><span class="step-icon"><i></i></span><span><b>09</b> Celebrate Success</span></div>
  </div>

  <svg class="abs" style="left:0;top:0" width="1200" height="940" viewBox="0 0 1200 940">
    <g fill="none" stroke="#333" stroke-width="1.3" stroke-dasharray="4 3">
      <path d="M259 512v26M259 620v24M616 522v24M616 622v24M975 522v24M975 622v24"/>
      <path d="M259 757v22h154V481h14"/>
      <path d="M616 757v22h154V481h14"/>
    </g>
    <g fill="#333">
      <path d="M255 538h8l-4 6zM255 644h8l-4 6zM612 546h8l-4 6zM612 646h8l-4 6zM971 546h8l-4 6zM971 646h8l-4 6z"/>
      <path d="M427 477v8l6-4zM784 477v8l6-4z"/>
    </g>
  </svg>
</section>

<section class="projects">
  <h2 class="section-title abs"><span class="mark-dot"></span>Client Project</h2>
  <p class="projects-sub abs">The Morrowline process</p>
  <div class="card abs" style="left:113px">
    <div class="card-photo" role="img" aria-label="Photo of a client at a wooden reception counter" style="background:linear-gradient(#e7ddc6,#b98a5a 55%,#7a5032)"></div>
    <h3>Launch Project</h3><p>Deep-dive session into<br>Project needs and goals</p>
  </div>
  <div class="card abs" style="left:444px">
    <div class="card-photo" role="img" aria-label="Photo of a waiting room with red chairs" style="background:linear-gradient(#e9e2d4,#9a7b63 55%,#6b2a2a)"></div>
    <h3>Determine Goal</h3><p>Deep-dive to define<br>your brand's audience &amp; the<br>ideal pathway to success</p>
  </div>
  <div class="card abs" style="left:777px">
    <div class="card-photo" role="img" aria-label="Photo of a presenter at a whiteboard" style="background:linear-gradient(#f1efea,#b9b4ab 55%,#4e4a45)"></div>
    <h3 style="margin-top:38px">Formulate Plan</h3><p>Deep-dive to define<br>your brand's audience</p>
  </div>
</section>
<div class="btn abs">VIEW MORE
  <svg width="30" height="16" viewBox="0 0 30 16"><path d="M1 8h26M20 1l7 7-7 7" fill="none" stroke="#fff" stroke-width="2.2"/></svg>
</div>

<section class="testimonial">
  <div class="quote-mark abs">&ldquo;</div>
  <h2 class="section-title abs"><span class="mark-dot"></span>Testomonial</h2>
  <p class="testimonial-sub abs">What Our Clients say</p>
  <p class="testimonial-text abs">Lorem ipsum dolor sit amet, consectetur adipiscing elit. Integer vulputate nunc nec ligula viverra ultrices. Phasellus scelerisque luctus mi non venenatis. Morbi sapien enim, egestas et augue ac, aliquam mattis libero. Vestibulum non lacus vel eros suscipit commodo.</p>
  <div class="avatar abs" role="img" aria-label="Client portrait photo"></div>
  <div class="person abs"><b>Daniel Harlow</b><span>Managing Director</span></div>
  <svg class="abs" style="left:88px;top:330px" width="24" height="46" viewBox="0 0 24 46"><path d="M20 2L4 23l16 21" fill="none" stroke="#333" stroke-width="2"/></svg>
  <svg class="abs" style="left:1066px;top:330px" width="24" height="46" viewBox="0 0 24 46"><path d="M4 2l16 21L4 44" fill="none" stroke="#333" stroke-width="2"/></svg>
</section>
<div class="dots abs"><i></i><i></i><i class="on"></i><i></i><i></i></div>

<footer class="site-footer">
  <div class="foot-brand abs">Morrowline<br>Creative</div>
  <div class="social abs"><i></i><i></i><i></i><i></i></div>

  <div class="foot-col abs" style="left:387px;top:100px">
    <h4>QUICK LINKS</h4>
    <ul>
      <li><span class="dot"></span>Home</li>
      <li><span class="dot"></span>About Us</li>
      <li><span class="dot"></span>Services</li>
      <li><span class="dot"></span>Process</li>
      <li><span class="dot"></span>Client Projects</li>
    </ul>
  </div>

  <div class="foot-col abs" style="left:580px;top:100px">
    <h4>CONTACT US</h4>
    <div style="margin-top:26px">
      <div class="contact-row"><span class="ic"><svg width="12" height="12" viewBox="0 0 12 12"><path d="M2 1l2 0 1 3-1.5 1a7 7 0 0 0 3.5 3.5L8 7l3 1v2c0 1-1 1-1 1A9 9 0 0 1 1 2s0-1 1-1z" fill="#ddd"/></svg></span><span>CALL US<br>310.555.0182</span></div>
      <div class="contact-row"><span class="ic"><svg width="13" height="10" viewBox="0 0 13 10"><rect x=".5" y=".5" width="12" height="9" fill="none" stroke="#ddd"/><path d="M.5 .5l6 5 6-5" fill="none" stroke="#ddd"/></svg></span><span>EMAIL US<br>hello@morrowlinecreative.com</span></div>
      <div class="contact-row"><span class="ic"><svg width="10" height="13" viewBox="0 0 10 13"><path d="M5 12S1 7 1 4.5a4 4 0 0 1 8 0C9 7 5 12 5 12z" fill="#ddd"/><circle cx="5" cy="4.5" r="1.5" fill="#1b1b1b"/></svg></span><span>4120 Larkspur Ave Suite B<br>Bellmont, CA 90812</span></div>
    </div>
  </div>

  <div class="foot-col abs" style="left:875px;top:100px">
    <h4>OUR NEWSLETTER</h4>
    <p style="font-size:11.5px;line-height:15px;margin-top:26px">Subscribe our newsletter<br>to get the latest news.</p>
    <div class="news-input"></div>
    <div class="news-btn">SUBSCRIBE</div>
  </div>
</footer>
<div class="copyright abs">Copyright © 2024 All Rights Reserved By Company name</div>

</body>
</html>
```